Modern business card design for professional copywriter

I'd like a business card design that I can use to have my cards printed out by plink.com as a squared corners business card (see artwork and design guidelines here: https://help.plink.com/hc/en-gb/sections/300481726-PLINK-Product-Templates)

The design should be clean and modern and reflect the colours, tone and branding on my website: https://noravestrel.com.au

Target Market(s)

Professionals, B2B small business owners

Industry/Entity Type

Business

Contact Information for Business Card

Nora Vestrel
m: 0427 593 864
e: nora@noravestrel.com.au
w: noravestrel.com.au

Font styles to use
Sans Serif

Requirements
Must have
• Tagline: "Smart copywriting for clever business people"
• Brand colours: fd8000, 009984, 666666 and black
Nice to have

```html
<!DOCTYPE html>
<html lang="en">
<head>
<meta charset="utf-8">
<title>Nora Vestrel – Business Card</title>
<link rel="stylesheet" href="https://fonts.googleapis.com/css2?family=Questrial&family=Lato:wght@400;700&display=swap">
<style>
  :root {
    --orange: #f7902a;
    --orange-deep: #ef7a22;
    --orange-light: #f99a45;
    --teal: #009984;
    --grey: #666666;
    --ink: #111111;
    --paper: #ffffff;
    --canvas: #ececec;
  }
  * { box-sizing: border-box; margin: 0; padding: 0; }
  html, body { width: 1200px; height: 586px; overflow: hidden; }
  body {
    background: var(--canvas);
    font-family: "Lato", sans-serif;
    position: relative;
  }
  .card {
    position: absolute;
    top: 129px;
    width: 502px;
    height: 301px;
    overflow: hidden;
  }
  .card--front { left: 61px; }
  .card--back { left: 619px; background: var(--paper); }

  .front-texture {
    position: absolute; inset: 0;
    background: linear-gradient(135deg, var(--orange-light) 0%, var(--orange) 45%, var(--orange-deep) 100%);
  }
  .brand {
    position: absolute;
    font-family: "Questrial", sans-serif;
    text-align: right;
    white-space: nowrap;
  }
  .brand-name { display: block; line-height: 1; }
  .brand-role { display: block; }

  .front-brand {
    left: 0; right: 0; top: 124px;
    display: flex; justify-content: center;
    color: var(--paper);
  }
  .front-brand .brand-inner { text-align: right; }
  .front-brand .brand-name { font-size: 58px; letter-spacing: -0.5px; }
  .front-brand .brand-role { font-size: 15px; letter-spacing: 8.6px; margin-top: 2px; margin-right: -8px; }

  .side-bar {
    position: absolute;
    top: 28px;
    width: 22px;
    height: 245px;
    background: var(--orange);
  }
  .side-bar--left { left: 0; border-radius: 0 10px 10px 0; }
  .side-bar--right { right: 0; border-radius: 10px 0 0 10px; }

  .back-brand {
    left: 0; right: 0; top: 48px;
    display: flex; justify-content: center;
    color: var(--teal);
  }
  .back-brand .brand-inner { text-align: right; }
  .back-brand .brand-name { font-size: 37px; }
  .back-brand .brand-role { font-size: 10px; letter-spacing: 5.5px; margin-top: 1px; margin-right: -5px; color: var(--grey); }

  .social-row {
    position: absolute; left: 42px; top: 177px;
    display: flex; gap: 7px;
  }
  .social-dot { width: 20px; height: 20px; border-radius: 50%; background: var(--orange); }

  .contact-list {
    position: absolute; left: 42px; top: 204px;
    list-style: none;
  }
  .contact-item {
    display: flex; align-items: center; gap: 7px;
    font-size: 12px; color: var(--ink);
    height: 24px;
  }
  .contact-icon { width: 17px; height: 17px; flex: none; }
  .contact-web {
    font-size: 12px; font-weight: 700; color: var(--teal);
    letter-spacing: 1px; margin-top: 2px;
  }

  .service-list {
    position: absolute; right: 36px; top: 159px;
    list-style: none; text-align: right;
  }
  .service-list li {
    font-size: 11px; font-weight: 700; color: var(--ink);
    line-height: 18.6px;
  }
</style>
</head>
<body>
  <section class="card card--front">
    <div class="front-texture" role="img" aria-label="Orange faceted low-poly background pattern"></div>
    <div class="brand front-brand">
      <div class="brand-inner">
        <span class="brand-name">Nora Vestrel</span>
        <span class="brand-role">COPYWRITER</span>
      </div>
    </div>
  </section>

  <section class="card card--back">
    <div class="side-bar side-bar--left"></div>
    <div class="side-bar side-bar--right"></div>

    <div class="brand back-brand">
      <div class="brand-inner">
        <span class="brand-name">Nora Vestrel</span>
        <span class="brand-role">COPYWRITER</span>
      </div>
    </div>

    <div class="social-row" aria-label="Social profiles">
      <span class="social-dot"></span>
      <span class="social-dot"></span>
      <span class="social-dot"></span>
      <span class="social-dot"></span>
    </div>

    <ul class="contact-list">
      <li class="contact-item">
        <svg class="contact-icon" viewBox="0 0 20 20" aria-hidden="true">
          <circle cx="10" cy="10" r="10" fill="#009984"/>
          <path d="M5 8.5c0-1.5 2.3-2.5 5-2.5s5 1 5 2.5v1h-2.5v-1.2h-5v1.2H5z M6.5 10.5h7l1 3.5h-9z" fill="#fff"/>
        </svg>
        <span>0427 593 864</span>
      </li>
      <li class="contact-item">
        <svg class="contact-icon" viewBox="0 0 20 20" aria-hidden="true">
          <circle cx="10" cy="10" r="10" fill="#009984"/>
          <rect x="5" y="6.5" width="10" height="7" fill="#fff"/>
          <path d="M5 6.5l5 4 5-4" fill="none" stroke="#009984" stroke-width="1"/>
        </svg>
        <span>nora@noravestrel.com.au</span>
      </li>
      <li class="contact-web">www.noravestrel.com.au</li>
    </ul>

    <ul class="service-list">
      <li>Feature Writing</li>
      <li>SEO Copywriting</li>
      <li>Legal Copywriting</li>
      <li>Content Marketing</li>
      <li>Website Copywriting</li>
      <li>Small Business Copywriting</li>
    </ul>
  </section>
</body>
</html>
```